Keys to business success

I love the principles of a book called "Where the quiet rivers bend toward home". I use the principles all the time at work. I'd like a poster made (map or web style design) to capture the books reminders. You can see a very basic verison of the design i'm looking for attached below "project summary".I've attached a word document of the text to include. Ive also attached two examples of the types of designs i'm looking for. The design will have to look modern and clear when printed on an 45.7 x 61 cm canvas.

Target Market(s)

Buisness people
Motivation

Industry/Entity Type

Business

Font styles to use
Serif

Requirements
Must have
• Web or map-like designs
• All 30 of the principles: 3 fonts (Title, sub-title and principles). The choice of fonts is up to the designer. No numbers for the principles.
• Professional feel
Nice to have
• Halos around phrases
Should not have
• No straight lines or ridgid concepts

```html
<!DOCTYPE html>
<html lang="en">
<head>
<meta charset="utf-8">
<title>30 Principles — Where the quiet rivers bend toward home</title>
<link rel="stylesheet" href="https://fonts.googleapis.com/css2?family=Playfair+Display:ital,wght@0,900;1,700&family=Cormorant+Garamond:ital,wght@0,700;1,600&family=Lora:wght@600&display=swap">
<style>
  :root {
    --paper: #ffffff;
    --ink: #111111;
    --text-light: #ffffff;

    --handling-label-top: #b8f8ff;
    --handling-label-bottom: #00c8f5;
    --handling-body-top: #0046d0;
    --handling-body-bottom: #021c55;
    --handling-line: #0a6fe0;

    --liking-label-top: #f6ff3a;
    --liking-label-bottom: #8cf000;
    --liking-body-top: #12e812;
    --liking-body-bottom: #075a1a;
    --liking-line: #2fc41a;

    --thinking-label-top: #ffff80;
    --thinking-label-bottom: #ffc400;
    --thinking-body-top: #ff6a00;
    --thinking-body-bottom: #ee0000;
    --thinking-line: #ff7a00;

    --leader-label-top: #ffb0da;
    --leader-label-bottom: #ff5f95;
    --leader-body-top: #f00060;
    --leader-body-bottom: #7a0012;
    --leader-line: #e0005a;

    --font-title: "Playfair Display", serif;
    --font-subtitle: "Cormorant Garamond", serif;
    --font-principle: "Lora", serif;
  }

  * { margin: 0; padding: 0; box-sizing: border-box; }

  html, body {
    width: 1200px;
    height: 899px;
    overflow: hidden;
    background: var(--paper);
  }

  .poster {
    position: relative;
    width: 1200px;
    height: 899px;
    background: var(--paper);
  }

  .connectors {
    position: absolute;
    inset: 0;
    width: 1200px;
    height: 899px;
    z-index: 0;
  }

  .connectors path {
    fill: none;
    stroke-width: 3;
    stroke-linecap: round;
    stroke-dasharray: 2 9;
  }

  .title-block {
    position: absolute;
    left: 4px;
    top: 250px;
    width: 262px;
    height: 400px;
    display: flex;
    flex-direction: column;
    align-items: center;
    justify-content: center;
    text-align: center;
    color: var(--ink);
    z-index: 1;
  }

  .title-halo {
    position: absolute;
    left: 6px;
    top: 25px;
    width: 250px;
    height: 350px;
    border-radius: 50%;
    background: radial-gradient(ellipse at center, #fff6e0 0%, #ffffff 70%);
    box-shadow: 0 0 0 2px #f1e3c6;
    z-index: -1;
  }

  .title-number {
    font-family: var(--font-title);
    font-weight: 900;
    font-size: 160px;
    line-height: 0.9;
    letter-spacing: -4px;
  }

  .title-main {
    font-family: var(--font-title);
    font-style: italic;
    font-weight: 700;
    font-size: 40px;
    line-height: 1.1;
    margin-top: 2px;
  }

  .title-sub {
    font-family: var(--font-subtitle);
    font-style: italic;
    font-weight: 600;
    font-size: 28px;
    line-height: 1.05;
    margin-top: 10px;
  }

  .group {
    position: absolute;
    left: 300px;
    width: 892px;
    z-index: 1;
    border-radius: 80px 36px 80px 36px / 60px 70px 60px 70px;
    box-shadow: 0 6px 18px rgba(0, 0, 0, 0.12);
  }

  .group-label {
    position: absolute;
    left: 12px;
    top: 50%;
    transform: translateY(-50%);
    width: 172px;
    display: flex;
    align-items: center;
    justify-content: center;
    text-align: center;
    padding: 0 18px;
    border-radius: 50%;
    font-family: var(--font-subtitle);
    font-weight: 700;
    font-size: 18px;
    line-height: 1.05;
    text-transform: uppercase;
    letter-spacing: 0.3px;
    color: var(--ink);
    box-shadow: 0 0 0 4px rgba(255, 255, 255, 0.35), 0 0 16px rgba(255, 255, 255, 0.45);
  }

  .principles {
    position: absolute;
    left: 204px;
    top: 50%;
    transform: translateY(-50%);
    list-style: none;
    font-family: var(--font-principle);
    font-weight: 600;
    font-size: 17px;
    line-height: 21.6px;
    color: var(--text-light);
    text-shadow: 0 0 8px rgba(255, 255, 255, 0.35), 0 1px 2px rgba(0, 0, 0, 0.25);
  }

  .principles li {
    position: relative;
    padding-left: 18px;
    white-space: nowrap;
  }

  .principles li::before {
    content: "";
    position: absolute;
    left: 0;
    top: 7px;
    width: 7px;
    height: 7px;
    border-radius: 50%;
    background: var(--bullet);
    box-shadow: 0 0 6px var(--bullet);
  }

  .handling { top: 8px;   height: 128px; background: linear-gradient(160deg, var(--handling-body-top), var(--handling-body-bottom)); --bullet: #5cc8ff; }
  .liking   { top: 146px; height: 166px; background: linear-gradient(160deg, var(--liking-body-top), var(--liking-body-bottom)); --bullet: #c8ff5a; }
  .thinking { top: 322px; height: 292px; background: linear-gradient(160deg, var(--thinking-body-top), var(--thinking-body-bottom)); --bullet: #ffe066; }
  .leader   { top: 624px; height: 268px; background: linear-gradient(160deg, var(--leader-body-top), var(--leader-body-bottom)); --bullet: #ffb3d6; }

  .handling .group-label { height: 108px; background: radial-gradient(circle at 40% 30%, var(--handling-label-top), var(--handling-label-bottom)); }
  .liking .group-label   { height: 130px; background: radial-gradient(circle at 40% 30%, var(--liking-label-top), var(--liking-label-bottom)); }
  .thinking .group-label { height: 150px; background: radial-gradient(circle at 40% 30%, var(--thinking-label-top), var(--thinking-label-bottom)); }
  .leader .group-label   { height: 130px; background: radial-gradient(circle at 40% 30%, var(--leader-label-top), var(--leader-label-bottom)); }

  .line-handling { stroke: var(--handling-line); }
  .line-liking   { stroke: var(--liking-line); }
  .line-thinking { stroke: var(--thinking-line); }
  .line-leader   { stroke: var(--leader-line); }
</style>
</head>
<body>
<main class="poster">
  <svg class="connectors" viewBox="0 0 1200 899" aria-hidden="true">
    <path class="line-handling" d="M 200 300 C 230 180, 250 72, 312 72"/>
    <path class="line-liking"   d="M 240 340 C 270 260, 270 229, 312 229"/>
    <path class="line-thinking" d="M 262 460 C 285 470, 290 468, 312 468"/>
    <path class="line-leader"   d="M 220 620 C 250 720, 262 758, 312 758"/>
  </svg>

  <header class="title-block">
    <div class="title-halo"></div>
    <div class="title-number">30</div>
    <h1 class="title-main">Principles</h1>
    <p class="title-sub">Where the quiet<br>rivers bend<br>toward home</p>
  </header>

  <section class="group handling">
    <h2 class="group-label">Fundamental techniques in handling people</h2>
    <ul class="principles">
      <li>Don't Criticize, Condemn or Complain</li>
      <li>Give Honest, Sincere, Appreciation</li>
      <li>Arouse In The Other Person An Eager Want</li>
    </ul>
  </section>

  <section class="group liking">
    <h2 class="group-label">Making people like you</h2>
    <ul class="principles">
      <li>Become Genuinely Interested In Other People</li>
      <li>Smile</li>
      <li>A Person's Name Is To That Person The Sweetest And Most Important Sound</li>
      <li>Be A Good Listener. Encourage Others To Talk About Themselves</li>
      <li>Talk In Terms Of The Other Person's Interests</li>
      <li>Make The Other Person Feel Important - And Do It Sincerely</li>
    </ul>
  </section>

  <section class="group thinking">
    <h2 class="group-label">Win people to your way of thinking</h2>
    <ul class="principles">
      <li>The Only Way To Get The Best Of An Argument Is To Avoid It</li>
      <li>Show Respect For The Other Person's Opinion. Never Say, "You're Wrong."</li>
      <li>If You Are Wrong Admit It Quickly And Emphatically</li>
      <li>Begin In A Friendly Manner</li>
      <li>Get The Other Person Saying "Yes, Yes"</li>
      <li>Let The Other Person Do A Great Deal Of The Talking</li>
      <li>Let The Other Person Feel That The Idea Is His Or Hers</li>
      <li>Try Honestly To See Things From The Other Person's Point Of View</li>
      <li>Be Sympathetic With The Other Person's Ideas And Desires</li>
      <li>Appeal To The Nobler Motives</li>
      <li>Dramatize Your Ideas</li>
      <li>Throw Down A Challenge</li>
    </ul>
  </section>

  <section class="group leader">
    <h2 class="group-label">Being a leader</h2>
    <ul class="principles">
      <li>Begin With Praise And Honest Appreciation</li>
      <li>Call Attention To People's Mistakes Indirectly</li>
      <li>Talk About Your Own Mistakes Before Criticizing The Other Person</li>
      <li>Ask Questions Instead Of Giving Direct Orders</li>
      <li>Let The Other Person Save Face</li>
      <li>Praise The Slightest Improvement And Praise Every Improvement.</li>
      <li>Give The Other Person A Fine Reputation To Live Up To</li>
      <li>Use Encouragement. Make The Fault Seem Easy To Correct</li>
      <li>Make The Other Person Happy About Doing The Thing You Suggest</li>
    </ul>
  </section>
</main>
</body>
</html>
```